Sumvane financial services stationery design

We need business stationery designed with letterheads, business cards, with compliments and envelope for a business that offers tax and accounting services

Designs look the same

Target Market(s)

Small to medium businesses, individuals, Self managed superfunds

Industry/Entity Type

Business

Font styles to use
Serif
Other font styles liked:
• Atlanta

Colors
32a6d6
3277b5

Requirements
Must have
• Logo incorporated with all my stationery
• professional
Should not have
• Lots of colours
• Busy

```html
<!DOCTYPE html>
<html lang="en">
<head>
<meta charset="utf-8">
<title>Sumvane Financial Services – Business Card</title>
<link href="https://fonts.googleapis.com/css2?family=Montserrat:wght@400;600;700&display=swap" rel="stylesheet">
<style>
  :root {
    --page-bg: #e4e4e8;
    --brand-blue: #2171b5;
    --brand-sky: #32a6d6;
    --card-white: #f1f1f3;
    --ink-grey: #4a4a4f;
    --text-light: #ffffff;
  }
  * { box-sizing: border-box; margin: 0; padding: 0; }
  html, body {
    width: 1200px;
    height: 1200px;
    overflow: hidden;
    background: var(--page-bg);
    font-family: "Montserrat", sans-serif;
  }
  .sheet {
    position: relative;
    width: 1200px;
    height: 1200px;
  }
  .card {
    position: absolute;
    left: 220px;
    width: 760px;
    height: 434px;
    overflow: hidden;
    box-shadow: 0 10px 30px rgba(0,0,0,0.12);
  }
  .card--front { top: 110px; background: var(--brand-blue); }
  .card--back  { top: 630px; background: var(--card-white); }

  .brand {
    position: absolute;
    display: flex;
    align-items: center;
    gap: 14px;
    white-space: nowrap;
  }
  .brand__square {
    width: 40px;
    height: 40px;
    background: var(--brand-sky);
  }
  .brand__name {
    font-size: 38px;
    font-weight: 600;
    letter-spacing: 2px;
    text-transform: uppercase;
  }
  .card--front .brand { left: 120px; top: 150px; }
  .card--front .brand__name { color: #d9dadd; }
  .card--back .brand { left: 60px; top: 96px; }
  .card--back .brand__name { color: var(--ink-grey); }

  .front__url {
    position: absolute;
    left: 250px;
    bottom: 60px;
    color: var(--text-light);
    font-size: 20px;
    font-weight: 400;
    letter-spacing: 0.5px;
  }

  .back__panel {
    position: absolute;
    inset: 0;
    background: var(--brand-blue);
    clip-path: polygon(72% 0, 100% 0, 100% 100%, 30% 100%);
  }
  .person {
    position: absolute;
    left: 340px;
    bottom: 46px;
    color: var(--text-light);
    white-space: nowrap;
  }
  .person__name { font-size: 28px; font-weight: 700; }
  .person__role { font-size: 22px; font-weight: 400; margin-top: 4px; }

  .contact {
    position: absolute;
    right: 40px;
    top: 140px;
    list-style: none;
    color: var(--text-light);
    font-size: 18px;
    white-space: nowrap;
  }
  .contact__item {
    display: flex;
    align-items: center;
    gap: 12px;
    height: 32px;
  }
  .contact__item svg { width: 16px; height: 16px; flex: none; }
  .contact__item--web { font-weight: 700; font-size: 19px; padding-left: 28px; }
</style>
</head>
<body>
<main class="sheet">
  <section class="card card--front" aria-label="Business card front">
    <div class="brand">
      <span class="brand__square"></span>
      <span class="brand__name">Sumvane</span>
    </div>
    <p class="front__url">www.sumvane.com</p>
  </section>

  <section class="card card--back" aria-label="Business card back">
    <div class="back__panel"></div>
    <div class="brand">
      <span class="brand__square"></span>
      <span class="brand__name">Sumvane</span>
    </div>
    <div class="person">
      <p class="person__name">Daniel Whitford</p>
      <p class="person__role">Director &amp; CEO</p>
    </div>
    <ul class="contact">
      <li class="contact__item">
        <svg viewBox="0 0 16 16" aria-hidden="true"><path fill="#fff" d="M3 1h3l1 4-2 1c1 2 2 3 4 4l1-2 4 1v3c0 1-1 2-2 2C7 14 2 9 1 3c0-1 1-2 2-2z"/></svg>
        <span>555.201.4470</span>
      </li>
      <li class="contact__item">
        <svg viewBox="0 0 16 16" aria-hidden="true"><rect x="4" y="1" width="8" height="14" rx="1.5" fill="none" stroke="#fff" stroke-width="1.6"/><circle cx="8" cy="12.5" r="0.9" fill="#fff"/></svg>
        <span>555.309.8812</span>
      </li>
      <li class="contact__item">
        <svg viewBox="0 0 16 16" aria-hidden="true"><rect x="1" y="3" width="14" height="10" fill="#fff"/><path d="M1 3l7 6 7-6" fill="none" stroke="#2171b5" stroke-width="1.4"/></svg>
        <span>hello@sumvane.com</span>
      </li>
      <li class="contact__item contact__item--web">www.sumvane.com</li>
    </ul>
  </section>
</main>
</body>
</html>
```